Business Card Design for Technology Company

New business card design needed for technology company director.
Ideally, the design will fit the style and nature of the industry. We are a supplier of quality products and services, and we hope the design will give customers and suppliers this impression.

Target Market(s)

3D Printing Industry

Industry/Entity Type

Technology Equipment

Contact Information for Business Card

Name: Marcus Lyle
Title: Director
Company address: Factory K4, 7B Morland Road, Kelvale Victoria Australia 3199
Telephone: +61-7-4620 6413
Email: marcus.lyle@veranox.com.au
Website: www.veranox.com.au

Requirements
Must have
• All information in business card details
• Company logo
• '3D Printers and 3D Print Filaments' at proper place
Nice to have
• Style to fit the industry
• Colour to fit logo

```html
<!DOCTYPE html>
<html lang="en">
<head>
<meta charset="utf-8">
<title>Veranox Technology – Business Card</title>
<link rel="stylesheet" href="https://fonts.googleapis.com/css2?family=Open+Sans:wght@400;600;700&display=swap">
<style>
  :root{
    --backdrop:#3b3c3f;
    --navy:#0d4a86;
    --blue:#1565a8;
    --blue-deep:#0a3f74;
    --orange:#f39200;
    --ink:#222326;
    --rule:#6b6d71;
    --paper:#ffffff;
    --paper-shade:#e9eaec;
  }
  *{margin:0;padding:0;box-sizing:border-box}
  html,body{width:1200px;height:1000px;overflow:hidden}
  body{background:var(--backdrop);font-family:"Open Sans",Arial,sans-serif;position:relative}

  .card{position:absolute;left:280px;width:640px;height:366px;overflow:hidden;box-shadow:0 10px 30px rgba(0,0,0,.45)}

  /* Back side */
  .card-back{top:60px;background:radial-gradient(ellipse at 50% 42%,#2a86cf 0%,var(--blue) 40%,var(--blue-deep) 100%)}
  .back-brand{position:absolute;top:120px;left:0;right:0;display:flex;justify-content:center;align-items:center;gap:14px}
  .brand-square{width:34px;height:34px;background:var(--orange)}
  .back-brand .brand-name{color:#fff;font-weight:700;font-size:40px;letter-spacing:8px}
  .back-rule{position:absolute;left:260px;top:206px;width:150px;height:1px;background:rgba(255,255,255,.75)}
  .tagline{position:absolute;top:222px;left:0;right:0;text-align:center;color:#fff;font-size:15px;letter-spacing:3px}

  /* Front side */
  .card-front{top:560px;background:linear-gradient(160deg,var(--paper) 45%,var(--paper-shade) 100%)}
  .front-brand{position:absolute;top:62px;right:38px;display:flex;align-items:center;gap:12px}
  .front-brand .brand-square{width:40px;height:40px;background:var(--blue)}
  .front-brand .brand-name{color:var(--ink);font-weight:700;font-size:22px;letter-spacing:4px}

  .person{position:absolute;left:32px;top:142px}
  .person-name{color:var(--navy);font-weight:700;font-size:22px;line-height:1}
  .person-title{color:var(--orange);font-size:14px;margin-top:3px;letter-spacing:.5px}

  .contact{position:absolute;left:32px;top:208px;list-style:none;font-size:15px;color:var(--ink)}
  .contact li{display:flex;align-items:center;gap:8px;height:22px}
  .contact svg{width:14px;height:14px;fill:var(--navy)}

  .address{position:absolute;right:32px;top:228px;text-align:right;font-size:16px;line-height:21px;color:#444;font-style:normal}
  .website{position:absolute;right:32px;top:332px;color:#fff;font-size:17px;letter-spacing:1.5px}

  .card-lines{position:absolute;inset:0}
</style>
</head>
<body>

<section class="card card-back">
  <div class="back-brand">
    <span class="brand-square"></span>
    <span class="brand-name">VERANOX</span>
  </div>
  <div class="back-rule"></div>
  <p class="tagline">3D Printers and 3D Print Filaments</p>
</section>

<section class="card card-front">
  <svg class="card-lines" viewBox="0 0 640 366" width="640" height="366">
    <line x1="32" y1="197" x2="620" y2="197" stroke="var(--rule)" stroke-width="0.8"/>
    <rect x="0" y="282" width="112" height="10" fill="#111"/>
    <rect x="112" y="282" width="112" height="10" fill="var(--orange)"/>
    <path d="M224 282 H320 L334 292 H224 Z" fill="#b8babd"/>
    <path d="M0 292 H330 C348 292 346 318 368 318 H640 V366 H0 Z" fill="var(--blue)"/>
  </svg>

  <div class="front-brand">
    <span class="brand-square"></span>
    <span class="brand-name">VERANOX TECHNOLOGY</span>
  </div>

  <div class="person">
    <h1 class="person-name">MARCUS LYLE</h1>
    <p class="person-title">DIRECTOR</p>
  </div>

  <ul class="contact">
    <li>
      <svg viewBox="0 0 16 16" aria-hidden="true"><path d="M3 1h3l1.5 4-2 1.3a9 9 0 0 0 4.2 4.2L11 8.5l4 1.5v3a2 2 0 0 1-2 2A12 12 0 0 1 1 3a2 2 0 0 1 2-2z"/></svg>
      <span>+61-7-4620 6413</span>
    </li>
    <li>
      <svg viewBox="0 0 16 16" aria-hidden="true"><path d="M1 3h14v1.2L8 9 1 4.2z"/><path d="M1 5.6 8 10.4l7-4.8V13H1z"/></svg>
      <span>marcus.lyle@veranox.com.au</span>
    </li>
  </ul>

  <address class="address">
    Factory K4, 7B Morland Road,<br>
    Kelvale Victoria<br>
    Australia 3199
  </address>

  <p class="website">www.veranox.com.au</p>
</section>

</body>
</html>
```